Book Cover " FROM GRAVEL TO AMBER"

Looking for a book cover for a novel from Gravel to Amber.
Amber is the characters developed name. The book describes his rough up bringing and how he obtains his greatness and his given name Amber.

```html
<!DOCTYPE html>
<html lang="en">
<head>
<meta charset="utf-8">
<title>From Gravel to Amber — Book Cover</title>
<link rel="stylesheet" href="https://fonts.googleapis.com/css2?family=Playfair+Display:wght@400;500&display=swap">
<style>
  :root {
    --parchment-light: #f0c56a;
    --parchment-mid: #e3a143;
    --parchment-deep: #c9772a;
    --foliage: #7d8a3a;
    --foliage-deep: #5a6a2a;
    --ink: #0d0f0a;
    --page-bg: #ffffff;
  }
  html, body {
    margin: 0;
    padding: 0;
    width: 800px;
    height: 1200px;
    overflow: hidden;
    background: var(--page-bg);
  }
  .cover {
    position: relative;
    width: 800px;
    height: 1200px;
    overflow: hidden;
    background:
      radial-gradient(ellipse at 20% 15%, rgba(160, 110, 50, 0.35), transparent 40%),
      radial-gradient(ellipse at 80% 90%, rgba(190, 100, 30, 0.4), transparent 50%),
      linear-gradient(180deg, var(--parchment-light) 0%, var(--parchment-mid) 55%, var(--parchment-deep) 100%);
  }
  .cover__art {
    position: absolute;
    left: 60px;
    top: 90px;
    width: 740px;
    height: 1110px;
    background:
      radial-gradient(ellipse at 45% 30%, rgba(125, 138, 58, 0.85), rgba(90, 106, 42, 0.55) 45%, transparent 72%),
      linear-gradient(180deg, transparent 55%, rgba(214, 128, 40, 0.55) 100%);
  }
  .cover__author {
    position: absolute;
    top: 40px;
    left: 0;
    width: 800px;
    text-align: center;
    font-family: "Playfair Display", serif;
    font-weight: 400;
    font-size: 34px;
    line-height: 1;
    letter-spacing: 0.95em;
    padding-left: 0.95em;
    box-sizing: border-box;
    color: var(--ink);
  }
  .cover__title {
    margin: 0;
    font-family: "Playfair Display", serif;
    font-weight: 500;
    color: var(--ink);
  }
  .cover__title-line {
    position: absolute;
    left: 0;
    width: 800px;
    text-align: center;
    line-height: 1;
    letter-spacing: -0.02em;
    white-space: nowrap;
  }
  .cover__title-line--from {
    top: 632px;
    font-size: 250px;
  }
  .cover__title-line--gravel {
    top: 871px;
    font-size: 125px;
  }
  .cover__title-line--amber {
    top: 1032px;
    font-size: 135px;
  }
</style>
</head>
<body>
  <main class="cover">
    <div class="cover__art" role="img" aria-label="Painted grove of tall bamboo stalks with green leafy crowns on a cracked, stained golden parchment wall"></div>
    <p class="cover__author">AUTHOR NAME</p>
    <h1 class="cover__title">
      <span class="cover__title-line cover__title-line--from">FROM</span>
      <span class="cover__title-line cover__title-line--gravel">GRAVEL</span>
      <span class="cover__title-line cover__title-line--amber">TO AMBER</span>
    </h1>
  </main>
</body>
</html>
```